Banners for Affiliate Marketing on Tantra website

We are starting an affiliate marketing program on our website brightmeadowhub.com and need banner ads for our affiliates. We are looking for the following sizes

for sure: 728x90, 300x250, 160x600
possibly: 468x60, 250x250, 125x125

Banner ads should market a several of our products - online tantra store, various tantra workshops, tantra vacations. See our website for details on what we offer.

For example, EITHER we may need one banner ad each in different sizes for:

Women's Workshop
Tantra Vacations
Tantric Massage workshop
Amber Harbor workshop
Sunrise & Willow Training
Selected products from our store, for example Quiet River Evenings DVD, or Milbrook Package

OR maybe we just need one banner ad in all the sizes for
Workshops
Store
Vacations

All images on our site can be used, or use other stock images.

The winner of this project will continue to work with us on graphic design of future banners, and we are also looking for a logo design.

Target Market(s)

couples, singles, age group 28-65, with disposable income

Industry/Entity Type

Graphic Design

Requirements
Must have
• Modern, attractive design that matches the branding and coloring on our website.
Should not have
• no obvious nudity in any graphics

```html
<!DOCTYPE html>
<html lang="en">
<head>
<meta charset="utf-8">
<title>Bright Meadow Institute – Affiliate Banners</title>
<link rel="stylesheet" href="https://fonts.googleapis.com/css2?family=Cinzel:wght@400;600&display=swap">
<style>
  :root {
    --stage: #111111;
    --ink-dark: #0d0b0b;
    --ink-text: #3a3330;
    --paper: #ffffff;
    --ribbon-red: #7a1414;
    --rule: #b9a99a;
    --sea: #8ccad3;
    --sand: #ece6d8;
    --skin: #d8c3ad;
    --font-display: "Cinzel", "Trajan Pro", serif;
  }
  * { box-sizing: border-box; margin: 0; padding: 0; }
  html, body { width: 1200px; height: 812px; overflow: hidden; background: var(--stage); }
  .canvas { position: relative; width: 1200px; height: 812px; font-family: var(--font-display); }

  .banner { position: absolute; overflow: hidden; background: var(--paper); }
  .banner--sky { left: 42px; top: 38px; width: 198px; height: 743px; }
  .banner--leader { left: 262px; top: 240px; width: 903px; height: 111px; }
  .banner--rect { left: 262px; top: 374px; width: 373px; height: 309px; }

  .photo { position: absolute; }
  .photo--beach-tall {
    left: 0; top: 0; width: 198px; height: 470px;
    background: linear-gradient(180deg, #9fd3da 0%, var(--sea) 45%, #d9e6e2 62%, var(--sand) 80%, var(--paper) 100%);
  }
  .photo--couple {
    left: 200px; top: 0; width: 400px; height: 111px;
    background: linear-gradient(90deg, #efe9e2 0%, var(--skin) 35%, #cdb49b 60%, #efece8 100%);
  }
  .photo--beach-wide {
    left: 0; top: 60px; width: 373px; height: 249px;
    background: linear-gradient(180deg, #cfe9ec 0%, var(--sea) 40%, #d2e3df 58%, var(--sand) 78%, #f4f0e6 100%);
  }

  .brand-panel { position: absolute; left: 0; top: 0; }
  .brand-panel svg { display: block; }
  .brand {
    position: absolute; color: var(--paper); font-weight: 400;
    text-align: center; line-height: 1.2; letter-spacing: 0.02em;
  }
  .brand__mark { display: block; margin: 0 auto 6px; border-radius: 50%; background: var(--paper); }

  .banner--sky .brand { left: 0; top: 14px; width: 198px; font-size: 19px; }
  .banner--sky .brand__mark { width: 22px; height: 22px; }
  .banner--leader .brand { left: 0; top: 10px; width: 200px; font-size: 17px; }
  .banner--leader .brand__mark { width: 18px; height: 18px; margin-bottom: 5px; }
  .rect-header {
    position: absolute; left: 0; top: 0; width: 373px; height: 69px;
    background: var(--ink-dark); display: flex; align-items: center; justify-content: center; gap: 12px;
  }
  .rect-header .brand { position: static; font-size: 18px; display: flex; align-items: center; gap: 12px; }
  .rect-header .brand__mark { width: 22px; height: 22px; margin: 0; }

  .offer { position: absolute; color: var(--ink-text); text-align: center; font-weight: 400; }
  .offer__line { display: block; }
  .offer__rule { display: block; height: 1px; background: var(--rule); margin: 4px auto; }

  .banner--sky .offer { left: 0; top: 462px; width: 198px; font-size: 27px; line-height: 51px; }
  .banner--leader .offer { left: 600px; top: 22px; width: 303px; font-size: 24px; line-height: 30px; }
  .banner--leader .offer__rule { width: 160px; margin: 1px auto 2px; }
  .banner--rect .offer { left: 95px; top: 88px; width: 270px; font-size: 22px; line-height: 28px; }
  .banner--rect .offer__rule { width: 140px; margin: 1px auto 2px; }

  .cta { position: absolute; display: block; }
  .banner--sky .cta { left: 14px; top: 660px; width: 174px; height: 70px; }
  .banner--rect .cta { left: 158px; top: 222px; width: 178px; height: 70px; }
  .cta text { font-family: var(--font-display); fill: var(--paper); font-size: 19px; letter-spacing: 0.02em; }
</style>
</head>
<body>
<main class="canvas">

  <!-- 160x600 skyscraper -->
  <section class="banner banner--sky" aria-label="Skyscraper banner">
    <div class="photo photo--beach-tall" role="img" aria-label="Couple sitting together on a tropical beach by turquoise water"></div>
    <div class="brand-panel">
      <svg width="198" height="230" viewBox="0 0 198 230" aria-hidden="true">
        <path d="M0 0 H198 V150 Q99 250 0 150 Z" fill="#0d0b0b"/>
      </svg>
    </div>
    <p class="brand"><span class="brand__mark"></span>Bright Meadow<br>Institute</p>
    <p class="offer">
      <span class="offer__line">Tantra</span>
      <span class="offer__line">Workshops</span>
      <span class="offer__line">Store</span>
      <span class="offer__line">Vacations</span>
    </p>
    <svg class="cta" viewBox="0 0 174 70" aria-label="Learn More">
      <rect x="4" y="40" width="16" height="22" fill="#7a1414"/>
      <rect x="154" y="6" width="16" height="22" fill="#7a1414"/>
      <path d="M10 16 C55 0 110 40 164 14 L164 50 C110 74 55 36 10 54 Z" fill="#0d0b0b"/>
      <path id="sky-cta-line" d="M18 36 C60 22 110 56 158 34" fill="none"/>
      <text><textPath href="#sky-cta-line" startOffset="50%" text-anchor="middle" dominant-baseline="middle">Learn More</textPath></text>
    </svg>
  </section>

  <!-- 728x90 leaderboard -->
  <section class="banner banner--leader" aria-label="Leaderboard banner">
    <div class="photo photo--couple" role="img" aria-label="Smiling mature couple leaning close together"></div>
    <div class="brand-panel">
      <svg width="240" height="111" viewBox="0 0 240 111" aria-hidden="true">
        <path d="M0 0 H205 Q240 55 205 111 H0 Z" fill="#0d0b0b"/>
      </svg>
    </div>
    <p class="brand"><span class="brand__mark"></span>Bright Meadow<br>Institute</p>
    <p class="offer">
      <span class="offer__line">Tantra Workshops</span>
      <span class="offer__rule"></span>
      <span class="offer__line">Store &amp; Vacation</span>
    </p>
  </section>

  <!-- 300x250 medium rectangle -->
  <section class="banner banner--rect" aria-label="Medium rectangle banner">
    <div class="photo photo--beach-wide" role="img" aria-label="Couple sitting on a white sand beach under palm fronds"></div>
    <header class="rect-header">
      <p class="brand"><span class="brand__mark"></span>Bright Meadow Institute</p>
    </header>
    <p class="offer">
      <span class="offer__line">Tantra Workshops</span>
      <span class="offer__rule"></span>
      <span class="offer__line">Store &amp; Vacation</span>
    </p>
    <svg class="cta" viewBox="0 0 178 70" aria-label="Learn More">
      <rect x="4" y="6" width="16" height="22" fill="#7a1414"/>
      <rect x="158" y="40" width="16" height="22" fill="#7a1414"/>
      <path d="M10 14 C60 2 112 24 168 18 L168 54 C112 62 60 38 10 50 Z" fill="#0d0b0b"/>
      <path id="rect-cta-line" d="M18 30 C62 20 112 40 162 38" fill="none"/>
      <text><textPath href="#rect-cta-line" startOffset="50%" text-anchor="middle" dominant-baseline="middle">Learn More</textPath></text>
    </svg>
  </section>

</main>
</body>
</html>
```